oN Hand Plus Project

We are a wireless internet service provider (WISP). We are launching a new service to our customers called "oN Hand Plus". This new program will provide the following services to our customers as part of the $8.95 monthly service fee:
In-Home service calls are free
Provide WiFi Router
Router Support and Configuration
Free Cable Move (1 per year)
Cable Repair
Anti-Virus protection software
We will also be offering these services for additional charges:
Internet Security Suite $4.95 /month
Online Backup Storage - $4.99 /month
Target Market(s)
Current customers that use our internet service.
Industry/Entity Type
Wireless Internet
Look and feel

```html
<!DOCTYPE html>
<html lang="en">
<head>
<meta charset="utf-8">
<title>oN Hand Plus – Mesa Breeze Wireless</title>
<link href="https://fonts.googleapis.com/css2?family=Arimo:wght@700&family=Roboto+Condensed:wght@700&display=swap" rel="stylesheet">
<style>
  :root {
    --sky-top: #1d9ad8;
    --sky-mid: #3eb2e8;
    --sky-low: #bfe6f8;
    --white: #ffffff;
    --navy: #1b2a7a;
    --navy-deep: #0f1d66;
    --red: #e0102a;
    --title-shadow: #1677b5;
  }
  * { margin: 0; padding: 0; box-sizing: border-box; }
  html, body { width: 848px; height: 1200px; overflow: hidden; background: var(--white); }
  .flyer {
    position: relative; width: 848px; height: 1200px; overflow: hidden;
    font-family: "Arimo", Arial, sans-serif; font-weight: 700;
    background: linear-gradient(180deg, var(--sky-top) 0%, var(--sky-mid) 45%, var(--sky-low) 80%, var(--white) 100%);
  }
  .top-curve { position: absolute; left: 0; top: 0; width: 848px; height: 230px; }
  .brand {
    position: absolute; top: 120px; left: 0; width: 848px; text-align: center;
    font-size: 34px; line-height: 1.15; color: var(--navy); letter-spacing: 1px;
  }
  .brand-dot {
    display: block; width: 48px; height: 48px; border-radius: 50%;
    background: var(--navy); margin: 0 auto 12px;
  }
  .brand { top: 62px; }
  .title {
    position: absolute; left: 0; width: 848px; text-align: center; color: var(--white);
    font-size: 124px; line-height: 1; letter-spacing: -1px;
    text-shadow: 4px 5px 0 var(--title-shadow);
  }
  .title.line-1 { top: 244px; left: 28px; }
  .title.line-2 { top: 344px; }
  .plan-heading {
    position: absolute; left: 78px; top: 460px; font-size: 53px; color: var(--red);
  }
  .plan-list { position: absolute; left: 78px; top: 542px; list-style: none; }
  .plan-list li { font-size: 26px; line-height: 33.5px; color: var(--navy); }
  .plan-list li::before { content: "• "; }
  .plan-list .free { color: var(--red); }
  .price {
    position: absolute; left: 590px; top: 610px; font-size: 84px; color: var(--white);
    transform: rotate(-17deg); transform-origin: left center;
    text-shadow: 3px 4px 0 var(--title-shadow);
  }
  .extras {
    position: absolute; left: 70px; top: 758px; width: 712px; height: 110px;
    border-radius: 22px 22px 0 0; border: 3px solid var(--white); border-bottom: none;
    background: linear-gradient(180deg, var(--navy) 0%, var(--navy-deep) 100%);
    font-family: "Roboto Condensed", "Arial Narrow", sans-serif; color: var(--white);
  }
  .extras-label { position: absolute; left: 24px; top: 24px; font-size: 22px; line-height: 28px; text-align: right; }
  .extra { position: absolute; top: 12px; }
  .extra.security { left: 238px; }
  .extra.backup { left: 476px; }
  .extra-name { font-size: 23px; }
  .extra-cost { font-size: 46px; line-height: 46px; }
  .extra-cost small { font-size: 22px; margin-left: 6px; }
  .photo-frame {
    position: absolute; left: 56px; top: 862px; width: 740px; height: 242px;
    background: var(--white); border-radius: 22px; padding: 12px;
  }
  .photo {
    position: relative; width: 100%; height: 100%; border-radius: 12px;
    background: linear-gradient(90deg, #a9a196 0%, #d6cfc2 30%, #eef2f4 52%, #e7eef3 75%, #9cc3df 100%);
  }
  .photo-caption {
    position: absolute; left: 320px; top: 18px; font-size: 25px; line-height: 31px; color: var(--navy);
  }
  .web { position: absolute; left: 72px; top: 1140px; font-size: 22px; color: var(--red); }
  .phones { position: absolute; left: 470px; top: 1122px; font-size: 23px; line-height: 31px; color: var(--navy); }
</style>
</head>
<body>
<main class="flyer">
  <svg class="top-curve" viewBox="0 0 848 230" aria-hidden="true">
    <path d="M0 0H848V170Q424 250 0 150Z" fill="#ffffff"/>
  </svg>

  <div class="brand"><span class="brand-dot"></span>Mesa Breeze Wireless</div>

  <h1 class="title line-1">oN Hand</h1>
  <div class="title line-2">Plus</div>

  <h2 class="plan-heading">Service plan includes:</h2>
  <ul class="plan-list">
    <li><span class="free">FREE</span> In-Home service calls</li>
    <li><span class="free">FREE</span> WiFi Router</li>
    <li><span class="free">FREE</span> Router Support and Configuration</li>
    <li><span class="free">FREE</span> Cable Move (1 per year)</li>
    <li><span class="free">FREE</span> Cable Repair</li>
    <li><span class="free">FREE</span> Anti-Virus software</li>
  </ul>

  <div class="price">$8.95</div>

  <section class="extras">
    <div class="extras-label">Additional Services<br>Available</div>
    <div class="extra security">
      <div class="extra-name">Internet Security Suite</div>
      <div class="extra-cost">$4.95<small>/month</small></div>
    </div>
    <div class="extra backup">
      <div class="extra-name">Online Backup Storage</div>
      <div class="extra-cost">$4.99<small>/month</small></div>
    </div>
  </section>

  <div class="photo-frame">
    <div class="photo" role="img" aria-label="Photo of a father and son using a laptop at home, and a woman working on a laptop at a desk">
      <p class="photo-caption">Wireless internet<br>for your home<br>and business</p>
    </div>
  </div>

  <div class="web">www.mbreezewireless.net</div>
  <div class="phones">(509) 555-0142 - Office<br>(509) 555-0187 - Support</div>
</main>
</body>
</html>
```